Construction Company

Design a clutter free business card, it can be double-sided utilizing the logo for BNX Ltd simple with all relevant contact information.

Please also a letterhead design to function for the purposes of invoicing, all mail requirements, with header to be distinctive while the footer ties page together and incorporates all necessary information.

For now, please use generic / dummy text and when a winner is selected, I will disclose the contact information.

Hi Designers! Please read the updated brief which includes the design of a business card and letterhead. Thank you!

```html
<!DOCTYPE html>
<html lang="en">
<head>
<meta charset="utf-8">
<title>BNX Ltd — Business Card</title>
<link rel="stylesheet" href="https://fonts.googleapis.com/css2?family=Libre+Baskerville:wght@400;700&family=Arimo:wght@400&display=swap">
<style>
  :root {
    --backdrop: #2a2a2a;
    --brand-blue: #023391;
    --brand-gold: #b38c07;
    --paper: #ffffff;
    --ink: #1a1a1a;
    --rule: #cfcfcf;
  }
  * { box-sizing: border-box; margin: 0; padding: 0; }
  html, body {
    width: 1200px; height: 1015px; overflow: hidden;
    background: var(--backdrop);
  }
  .canvas { position: relative; width: 1200px; height: 1015px; }
  .card {
    position: absolute; left: 220px; width: 760px; height: 434px;
    overflow: hidden;
    box-shadow: 0 10px 30px rgba(0,0,0,0.55);
  }
  .card--back { top: 50px; background: var(--brand-blue); }
  .card--front { top: 531px; background: var(--paper); }

  .wordmark {
    position: absolute;
    display: flex; align-items: center; gap: 14px;
    font-family: "Libre Baskerville", Georgia, serif;
    font-weight: 400; letter-spacing: 1px; white-space: nowrap;
  }
  .wordmark__dot { width: 22px; height: 22px; border-radius: 50%; background: var(--brand-gold); }
  .card--back .wordmark {
    left: 50%; top: 50%; transform: translate(-50%, -50%);
    font-size: 78px; color: var(--paper);
  }
  .card--front .wordmark {
    left: 200px; top: 196px; transform: translate(-50%, -50%);
    font-size: 52px; color: var(--brand-blue); gap: 12px;
  }
  .card--front .wordmark__dot { width: 16px; height: 16px; }

  .divider {
    position: absolute; left: 400px; top: 70px; width: 1px; height: 260px;
    background: var(--rule);
  }
  .contact {
    position: absolute; left: 432px; top: 70px; right: 20px;
    font-family: Arimo, Arial, sans-serif; color: var(--ink);
  }
  .contact__name {
    font-family: "Libre Baskerville", Georgia, serif; font-weight: 700;
    font-size: 21px; color: var(--brand-blue); letter-spacing: 0.5px;
  }
  .contact__role { font-size: 18px; margin-top: 4px; }
  .contact__list { list-style: none; margin-top: 20px; }
  .contact__item {
    display: flex; align-items: center; gap: 12px;
    font-size: 18px; line-height: 28px;
  }
  .contact__icon { width: 18px; height: 18px; flex: none; fill: var(--brand-blue); }
  .contact__link-accent { color: var(--brand-blue); }
  .contact__address { font-size: 18px; line-height: 24px; margin-top: 18px; }

  .band { position: absolute; bottom: 0; }
  .band--blue { left: 0; width: 430px; height: 14px; background: var(--brand-blue); }
  .band--gold { left: 436px; right: 0; height: 60px; background: var(--brand-gold); }
</style>
</head>
<body>
<main class="canvas">
  <section class="card card--back" aria-label="Card back">
    <div class="wordmark"><span class="wordmark__dot"></span>BNX Ltd</div>
  </section>

  <section class="card card--front" aria-label="Card front">
    <div class="wordmark"><span class="wordmark__dot"></span>BNX Ltd</div>
    <div class="divider"></div>
    <div class="contact">
      <p class="contact__name">DANIEL HARPER</p>
      <p class="contact__role">Managing Director</p>
      <ul class="contact__list">
        <li class="contact__item">
          <svg class="contact__icon" viewBox="0 0 24 24"><path d="M6.6 10.8a15.1 15.1 0 0 0 6.6 6.6l2.2-2.2c.3-.3.7-.4 1-.2 1.1.4 2.3.6 3.6.6.6 0 1 .4 1 1V20c0 .6-.4 1-1 1A17 17 0 0 1 3 4c0-.6.4-1 1-1h3.5c.6 0 1 .4 1 1 0 1.3.2 2.5.6 3.6.1.3 0 .7-.2 1z"/></svg>
          020-555 014 276
        </li>
        <li class="contact__item">
          <svg class="contact__icon" viewBox="0 0 24 24"><path d="M7 2h10a2 2 0 0 1 2 2v16a2 2 0 0 1-2 2H7a2 2 0 0 1-2-2V4a2 2 0 0 1 2-2zm0 3v12h10V5zm5 13.5a1 1 0 1 0 0 2 1 1 0 0 0 0-2z"/></svg>
          020-555 014 389
        </li>
        <li class="contact__item">
          <svg class="contact__icon" viewBox="0 0 24 24"><path d="M2 5h20v14H2zm2 2v.5l8 5 8-5V7l-8 5z"/></svg>
          hello@bnxltd.com
        </li>
        <li class="contact__item">
          <svg class="contact__icon" viewBox="0 0 24 24"><path d="M12 2a10 10 0 1 0 0 20 10 10 0 0 0 0-20zm6.9 9h-3a15 15 0 0 0-1.3-5.9A8 8 0 0 1 18.9 11zM12 4c.9 1.2 1.8 3.7 1.9 7h-3.8c.1-3.3 1-5.8 1.9-7zM4.1 13h3a15 15 0 0 0 1.3 5.9A8 8 0 0 1 4.1 13zm3-2h-3a8 8 0 0 1 4.3-5.9A15 15 0 0 0 7.1 11zM12 20c-.9-1.2-1.8-3.7-1.9-7h3.8c-.1 3.3-1 5.8-1.9 7zm2.6-1.1a15 15 0 0 0 1.3-5.9h3a8 8 0 0 1-4.3 5.9z"/></svg>
          <span>www.<span class="contact__link-accent">bnxltd</span>.com</span>
        </li>
      </ul>
      <p class="contact__address">17 Harbour Road, Northgate<br>NG4 2LT, United Kingdom</p>
    </div>
    <div class="band band--blue"></div>
    <div class="band band--gold"></div>
  </section>
</main>
</body>
</html>
```